Building Servicess

We need a new business card design for a company. We specialise in: Electrical/Site temporary electrics, Data/Network Installation, Passive Fire Protection

Industry/Entity Type

Construction

Contact Information for Business Card

Services provided as detailed on project description

Font styles to use
Serif

Colors
0054AA
0677BA
7BADD7
CADEEF
E8F1F8
00AB8E
00BBA5
67D7C9
C6EFE9
E9F9F6
EB3D1F
EC4F4E
F09395
F8D3D4
FCEDEE

Requirements
Must have
• Company logo-contact details-phone numbers

```html
<!DOCTYPE html>
<html lang="en">
<head>
<meta charset="utf-8">
<title>Harbor Build Services – Business Card</title>
<link rel="stylesheet" href="https://fonts.googleapis.com/css2?family=Libre+Baskerville:wght@400;700&display=swap">
<style>
  :root {
    --page-bg: #d9dcdf;
    --card-grey: #5e5f61;
    --brand-blue: #0f5aa8;
    --brand-blue-deep: #0054aa;
    --paper-white: #f7f7f5;
    --text-light: #ffffff;
    --text-muted: #e3e5e8;
    --text-services: #4a4c50;
  }
  * { margin: 0; padding: 0; box-sizing: border-box; }
  html, body {
    width: 1200px;
    height: 1200px;
    overflow: hidden;
    background: var(--page-bg);
    font-family: "Libre Baskerville", serif;
  }
  .canvas {
    position: relative;
    width: 1200px;
    height: 1200px;
  }
  .card {
    position: absolute;
    left: 250px;
    width: 700px;
    height: 400px;
    overflow: hidden;
    box-shadow: 0 18px 40px rgba(0, 0, 0, 0.18);
  }
  .card--front { top: 170px; background: var(--card-grey); }
  .card--back  { top: 630px; background: var(--brand-blue); }

  .card__shapes {
    position: absolute;
    inset: 0;
    width: 700px;
    height: 400px;
  }

  .holder {
    position: absolute;
    left: 44px;
    top: 150px;
    color: var(--text-light);
    white-space: nowrap;
  }
  .holder__name {
    font-size: 24px;
    letter-spacing: 1px;
    line-height: 1;
    font-weight: 400;
  }
  .holder__name strong { font-weight: 700; }
  .holder__role {
    margin-top: 10px;
    font-size: 15px;
    font-weight: 400;
    letter-spacing: 1.5px;
  }

  .contact {
    position: absolute;
    left: 44px;
    bottom: 34px;
    list-style: none;
    color: var(--text-muted);
    font-size: 13px;
    font-weight: 400;
    line-height: 1.85;
    white-space: nowrap;
  }

  .brand {
    position: absolute;
    display: flex;
    align-items: center;
    gap: 14px;
    font-weight: 700;
    text-transform: uppercase;
    line-height: 1.2;
    white-space: nowrap;
  }
  .brand__mark { flex: none; }
  .brand--front {
    right: 40px;
    top: 82px;
    color: var(--brand-blue-deep);
    font-size: 16px;
    letter-spacing: 0.5px;
  }
  .brand--front .brand__mark {
    width: 34px; height: 34px;
    background: var(--brand-blue-deep);
  }

  .services {
    position: absolute;
    right: 40px;
    bottom: 36px;
    list-style: none;
    text-align: right;
    color: var(--text-services);
    font-size: 11.5px;
    line-height: 1.8;
    white-space: nowrap;
  }

  .brand--back {
    left: 50%;
    top: 50%;
    transform: translate(-50%, -50%);
    color: var(--text-light);
    font-size: 30px;
    letter-spacing: 1px;
    gap: 20px;
  }
  .brand--back .brand__mark {
    width: 64px; height: 64px;
    background: var(--text-light);
  }
</style>
</head>
<body>
<main class="canvas">

  <section class="card card--front" aria-label="Business card front">
    <svg class="card__shapes" viewBox="0 0 700 400" aria-hidden="true">
      <polygon class="band-blue" points="380,0 700,0 700,400 420,400 250,250" fill="#0f5aa8"/>
      <line class="band-edge" x1="236" y1="249" x2="413" y2="405" stroke="#f7f7f5" stroke-width="5"/>
      <polygon class="panel-white" points="460,0 700,0 700,400 505,400 335,250" fill="#f7f7f5"/>
    </svg>

    <div class="holder">
      <h1 class="holder__name"><strong>DANIEL</strong>REEVE</h1>
      <p class="holder__role">OWNER</p>
    </div>

    <ul class="contact">
      <li class="contact__phone">555-014-2780</li>
      <li class="contact__email">info@harborbuild.com</li>
    </ul>

    <div class="brand brand--front">
      <span class="brand__mark"></span>
      <span class="brand__name">Harbor Build<br>Services Ltd</span>
    </div>

    <ul class="services">
      <li>Electrical &amp; Temporary Site Electrics</li>
      <li>Data &amp; Network Installation</li>
      <li>Passive Fire Protection</li>
    </ul>
  </section>

  <section class="card card--back" aria-label="Business card back">
    <div class="brand brand--back">
      <span class="brand__mark"></span>
      <span class="brand__name">Harbor Build<br>Services Ltd</span>
    </div>
  </section>

</main>
</body>
</html>
```